5 Planner Covers for Teacher Planners

Hello,
I currently run a Speech-Language Pathologist website and have created a planner for my fellow Speech Therapist. I would like someone to create 5 different planner covers so my followers will have different options to choose from.
Here is my planner from last year to give you an idea of what the planner will look like http://www.talkwellnook.example/free-slp-planner/
My followers are mostly women aged 25-50. However, I don't want the covers to be overly girly or excessive with flowers. Simple is better.
I'd also like there to be an editable text box to allow the Speech Therapist to type their name on their cover if they wish.
Planner Cover can say any of the following: SLP Planner, Planner, Speech Therapy Planner, Speech-Language Pathologist (maybe this title could be editable as well??).
To give you an idea I have uploaded a screenshot of last year's planners cover that I made myself.
What I am looking for:
-Size 8.5" by 11"
-5 different planner covers
-1 gender-neutral cover
-simple design
-limited flowers (or overly girly
-text box to add a personal name
-Possible titles: SLP Planner, Planner, Speech Therapy Planner, Speech-Language Pathologist (maybe this title could be editable as well??)
Target Market(s)
Women aged 25-50
Colors
Designer to choose colors to be used in the design.
Requirements
Must have
- What I am looking for:
-Size 8.5" by 11"
-1 gender-neutral cover
-simple design
Nice to have
- I've uploaded some that I like from Craftly to give you an idea.
Here is my craftly store https://www.craftly.example/shop/QuietMeadowHome to give you an idea of things I like.
I like Marla Hensley and her simple elegant rustic style.

```html
<!DOCTYPE html>
<html lang="en">
<head>
<meta charset="utf-8">
<title>SLP Planner Cover</title>
<link rel="stylesheet" href="https://fonts.googleapis.com/css2?family=Amatic+SC:wght@400;700&family=Josefin+Sans:wght@400&display=swap">
<style>
  :root {
    --pink-deep: #d98ca6;
    --pink-mid: #eab3c0;
    --pink-soft: #f3d3d6;
    --lavender: #e7c6e6;
    --cream: #f4e9da;
    --gold: #e3c235;
    --gold-line: #e2b53a;
    --ink: #2b2b2b;
  }
  * { margin: 0; padding: 0; box-sizing: border-box; }
  html, body { width: 927px; height: 1200px; overflow: hidden; }
  .cover {
    position: relative;
    width: 927px;
    height: 1200px;
    overflow: hidden;
    background:
      radial-gradient(ellipse 300px 260px at 80px 120px, var(--lavender), transparent 70%),
      radial-gradient(ellipse 320px 300px at 760px 620px, var(--cream), transparent 70%),
      radial-gradient(ellipse 360px 300px at 640px 1050px, var(--pink-deep), transparent 70%),
      radial-gradient(ellipse 280px 260px at 120px 500px, var(--pink-mid), transparent 70%),
      radial-gradient(ellipse 300px 240px at 300px 260px, var(--pink-mid), transparent 70%),
      linear-gradient(160deg, var(--pink-soft) 0%, var(--pink-mid) 45%, var(--pink-soft) 70%, var(--pink-mid) 100%);
  }
  .splatter {
    position: absolute;
    border-radius: 50%;
  }
  .splatter--top {
    left: 560px; top: 22px; width: 350px; height: 440px;
    background: radial-gradient(ellipse at 55% 45%, rgba(227,194,53,0.55), rgba(227,194,53,0.15) 55%, transparent 72%);
  }
  .splatter--bottom {
    left: 0; top: 814px; width: 315px; height: 350px;
    background: radial-gradient(ellipse at 45% 50%, rgba(227,194,53,0.5), rgba(227,194,53,0.12) 55%, transparent 72%);
  }
  .wreath {
    position: absolute;
    left: 205px; top: 318px;
    width: 520px; height: 520px;
  }
  .title-block {
    position: absolute;
    left: 0; width: 927px;
    text-align: center;
    color: var(--ink);
  }
  .title {
    top: 505px;
    font-family: "Amatic SC", cursive;
    font-weight: 700;
    font-size: 64px;
    letter-spacing: 5px;
    line-height: 1;
  }
  .owner-label {
    top: 612px;
    font-family: "Josefin Sans", sans-serif;
    font-variant: small-caps;
    font-size: 22px;
    letter-spacing: 2px;
    line-height: 1;
  }
  .owner-name {
    top: 636px;
    font-family: "Amatic SC", cursive;
    font-weight: 400;
    font-size: 58px;
    letter-spacing: 3px;
    line-height: 1;
  }
</style>
</head>
<body>
  <main class="cover">
    <div class="splatter splatter--top" role="img" aria-label="Gold foil paint splatter"></div>
    <div class="splatter splatter--bottom" role="img" aria-label="Gold foil paint splatter"></div>

    <svg class="wreath" viewBox="0 0 520 520" role="img" aria-label="Gold ring wreath with leaf sprigs">
      <defs>
        <radialGradient id="foliage" cx="50%" cy="50%" r="50%">
          <stop offset="80%" stop-color="#e9b7a6" stop-opacity="0"/>
          <stop offset="92%" stop-color="#e9b7a6" stop-opacity="0.45"/>
          <stop offset="100%" stop-color="#e9b7a6" stop-opacity="0"/>
        </radialGradient>
      </defs>
      <circle cx="260" cy="260" r="255" fill="url(#foliage)"/>
      <circle cx="262" cy="258" r="236" fill="none" stroke="var(--gold-line)" stroke-width="2.5"/>
      <circle cx="256" cy="263" r="229" fill="none" stroke="var(--gold-line)" stroke-width="1.8"/>
      <circle cx="260" cy="260" r="222" fill="none" stroke="var(--gold-line)" stroke-width="1.2" opacity="0.8"/>
    </svg>

    <h1 class="title-block title">SLP Planner</h1>
    <p class="title-block owner-label">Property Of</p>
    <p class="title-block owner-name">Dana Whitcombe</p>
  </main>
</body>
</html>
```